Vorna Fleet business card

I am needing a business card that at a glance shows all the services that we provide emphasizing some more than others. We are a Fleet and Compliance management company as well as a software company. We provide outsourced solutions for KPX compliance and HR services via our own software.
In addition, we do
drug testing
GPS
Cameras
Electronic DVIRS
ELD's

Target Market(s)

Transportation company owners

Industry/Entity Type

Transportation supplier

Contact Information for Business Card

the card should inform potential customers what we do

Other font styles liked:
• I have added brand guidelines. See attached

Requirements
Must have
• See description
Should not have
• Colors outside my brand guide. See attached

```html
<!DOCTYPE html>
<html lang="en">
<head>
<meta charset="utf-8">
<title>Vorna Fleet business card</title>
<link rel="stylesheet" href="https://fonts.googleapis.com/css2?family=Oswald:wght@600&family=Montserrat:wght@400;700&family=Roboto:wght@400&display=swap">
<style>
  :root {
    --bg: #9a9a9a;
    --card: #2a2a2c;
    --card-back: #1f1f21;
    --red: #ff1f2b;
    --band: #e4e5e7;
    --band-text: #3a3a3c;
    --light: #d9d9d9;
    --muted: #c8c8ca;
  }
  * { box-sizing: border-box; margin: 0; padding: 0; }
  html, body { width: 1200px; height: 800px; overflow: hidden; }
  body {
    background: var(--bg);
    display: flex;
    align-items: center;
    justify-content: center;
    gap: 40px;
  }
  .card {
    position: relative;
    width: 550px;
    height: 314px;
    border-bottom: 2px solid var(--red);
    border-right: 2px solid var(--red);
    overflow: hidden;
  }
  .card--front { background: var(--card); }
  .card--back { background: var(--card-back); display: flex; align-items: center; justify-content: center; }

  .identity {
    position: absolute;
    top: 98px;
    left: 0;
    right: 0;
    display: flex;
    justify-content: center;
    align-items: center;
    gap: 22px;
  }
  .person { text-align: right; }
  .person__name {
    font-family: "Oswald", sans-serif;
    font-weight: 600;
    font-size: 26px;
    line-height: 1;
    color: var(--red);
    letter-spacing: 0.5px;
  }
  .person__role {
    font-family: "Montserrat", sans-serif;
    font-size: 12px;
    color: var(--red);
    margin-top: 3px;
  }
  .divider { width: 1px; height: 58px; background: #5a5a5c; }
  .contacts { list-style: none; font-family: "Montserrat", sans-serif; font-size: 12.5px; color: var(--muted); }
  .contacts li { display: flex; align-items: center; gap: 8px; line-height: 19px; }
  .contacts svg { width: 11px; height: 11px; fill: var(--red); flex: none; }

  .tagline {
    position: absolute;
    top: 196px;
    left: 0;
    right: 0;
    display: flex;
    align-items: center;
    justify-content: center;
    gap: 10px;
    font-family: "Montserrat", sans-serif;
    font-weight: 700;
    font-size: 13px;
    color: var(--red);
    letter-spacing: 0.3px;
  }
  .tagline::before, .tagline::after { content: ""; width: 70px; height: 1.5px; background: var(--red); }

  .services-band {
    position: absolute;
    top: 228px;
    left: 0;
    right: 0;
    height: 40px;
    background: var(--band);
    display: flex;
    align-items: center;
    justify-content: center;
    font-family: "Roboto", sans-serif;
    font-size: 12.5px;
    color: var(--band-text);
    white-space: nowrap;
  }

  .brand-name {
    font-family: "Montserrat", sans-serif;
    font-weight: 700;
    font-size: 44px;
    letter-spacing: 2px;
    color: var(--light);
  }
</style>
</head>
<body>
  <section class="card card--front" aria-label="Card front">
    <div class="identity">
      <div class="person">
        <p class="person__name">DALE MORROW</p>
        <p class="person__role">CEO</p>
      </div>
      <div class="divider"></div>
      <ul class="contacts">
        <li>
          <svg viewBox="0 0 24 24" aria-hidden="true"><path d="M6.6 10.8a15.1 15.1 0 0 0 6.6 6.6l2.2-2.2a1 1 0 0 1 1-.25 11.4 11.4 0 0 0 3.6.57 1 1 0 0 1 1 1V20a1 1 0 0 1-1 1A17 17 0 0 1 3 4a1 1 0 0 1 1-1h3.5a1 1 0 0 1 1 1c0 1.25.2 2.45.57 3.6a1 1 0 0 1-.25 1z"/></svg>
          (480) 555-0172
        </li>
        <li>
          <svg viewBox="0 0 24 24" aria-hidden="true"><path d="M2 5h20v14H2z M2 5l10 8 10-8" stroke="#2a2a2c" stroke-width="1.5"/></svg>
          info@vornafleet.com
        </li>
        <li>
          <svg viewBox="0 0 24 24" aria-hidden="true"><circle cx="12" cy="12" r="10"/></svg>
          www.vornafleet.com
        </li>
      </ul>
    </div>
    <p class="tagline">COMPLIANCE MADE SIMPLE</p>
    <p class="services-band">Compliance | Fleet Management | Drug testing | GPS | Cameras | Electronic DVIRS | ELD's</p>
  </section>

  <section class="card card--back" aria-label="Card back">
    <p class="brand-name">Vorna Fleet</p>
  </section>
</body>
</html>
```